General contractor/GM consaltant business card

I need a card for my contracting company in North Dakota, we build industrial buildings for the oil feild and oil feild related companies offices, shops, airplain hangars, airports ext. We have a familly atmosphere on the job and are very relational and personal.
Industry/Entity Type
Industrial
Contact Information for Business Card
Kestrelmoor Builders LLC.
Dwight T.Halvorsun
4736 Quillfern dr. Colorado Springs, CO. 80927
Cell# 406-555-8142
dwight@kestrelmoorbuilders.com

```html
<!DOCTYPE html>
<html lang="en">
<head>
<meta charset="utf-8">
<title>Kestrelmoor Builders LLC – Business Card</title>
<link href="https://fonts.googleapis.com/css2?family=Roboto:wght@300;400;700&family=Arimo:wght@400&display=swap" rel="stylesheet">
<style>
  :root {
    --bg: #d9d9db;
    --card: #f7f7f7;
    --red: #e0262b;
    --blue: #2a5fb0;
    --navy: #1f3f8f;
    --ink: #1a1a1a;
    --shadow: rgba(0,0,0,0.18);
  }
  html, body {
    margin: 0;
    width: 1200px;
    height: 858px;
    overflow: hidden;
    background: var(--bg);
  }
  .canvas {
    position: relative;
    width: 1200px;
    height: 858px;
  }
  .card {
    position: absolute;
    top: 269px;
    width: 560px;
    height: 320px;
    background: var(--card);
    box-shadow: 0 8px 22px var(--shadow);
    overflow: hidden;
  }
  .card--front { left: 20px; }
  .card--back { left: 620px; }

  .brand {
    display: flex;
    align-items: center;
    gap: 8px;
    color: var(--red);
    font-family: "Roboto", sans-serif;
    font-weight: 700;
    white-space: nowrap;
  }
  .brand__mark {
    width: 12px;
    height: 12px;
    background: var(--blue);
    flex: none;
  }

  .identity {
    position: absolute;
    left: 26px;
    top: 112px;
    width: 280px;
  }
  .identity .brand {
    font-size: 21px;
    line-height: 28px;
  }
  .holder {
    margin: 26px 0 0 40px;
    font-family: "Roboto", sans-serif;
    font-weight: 300;
    font-size: 22px;
    line-height: 28px;
    color: var(--red);
    white-space: nowrap;
  }

  .divider {
    position: absolute;
    left: 318px;
    top: 100px;
    width: 1px;
    height: 120px;
    background: var(--ink);
  }

  .contacts {
    position: absolute;
    right: 24px;
    top: 116px;
    margin: 0;
    padding: 0;
    list-style: none;
    font-family: "Arimo", sans-serif;
    font-size: 12px;
    line-height: 19px;
    color: var(--navy);
    text-align: right;
    white-space: nowrap;
  }
  .contacts li {
    display: flex;
    justify-content: flex-end;
    align-items: flex-start;
    gap: 9px;
  }
  .contacts .icon {
    width: 10px;
    height: 10px;
    margin-top: 4px;
    flex: none;
  }
  .contacts .address { line-height: 17px; margin-top: 1px; }

  .card--back .brand {
    position: absolute;
    left: 0;
    right: 0;
    top: 134px;
    justify-content: center;
    gap: 12px;
    font-size: 38px;
    line-height: 50px;
  }
  .card--back .brand__mark {
    width: 20px;
    height: 20px;
  }
</style>
</head>
<body>
<main class="canvas">
  <section class="card card--front" aria-label="Business card front">
    <div class="identity">
      <div class="brand"><span class="brand__mark"></span>Kestrelmoor Builders LLC</div>
      <p class="holder">Dwight T.Halvorsun</p>
    </div>
    <span class="divider"></span>
    <ul class="contacts">
      <li><span>406-555-8142</span>
        <svg class="icon" viewBox="0 0 10 10" aria-hidden="true"><rect x="2" y="0.5" width="6" height="9" rx="1" fill="none" stroke="#1a1a1a" stroke-width="1.2"/><rect x="3" y="2" width="4" height="4.5" fill="#1a1a1a"/></svg></li>
      <li><span>dwight@kestrelmoorbuilders.com</span>
        <svg class="icon" viewBox="0 0 10 10" aria-hidden="true"><rect x="0.5" y="2" width="9" height="6.5" fill="#1a1a1a"/><path d="M0.5 2 L5 5.8 L9.5 2" fill="none" stroke="#f7f7f7" stroke-width="1"/></svg></li>
      <li><span class="address">4736 Quillfern dr.<br>Colorado Springs, CO. 80927</span>
        <svg class="icon" viewBox="0 0 10 10" aria-hidden="true"><path d="M5 0.5 C2.5 0.5 1.3 2.3 1.3 4 C1.3 6.3 5 9.5 5 9.5 C5 9.5 8.7 6.3 8.7 4 C8.7 2.3 7.5 0.5 5 0.5 Z" fill="#1a1a1a"/><circle cx="5" cy="3.9" r="1.3" fill="#f7f7f7"/></svg></li>
    </ul>
  </section>

  <section class="card card--back" aria-label="Business card back">
    <div class="brand"><span class="brand__mark"></span>Kestrelmoor Builders LLC</div>
  </section>
</main>
</body>
</html>
```